I need a new business card design for my pharmacy.

I need a business card design. I will include my logo.
The card needs to be readable. I prefer to have my logo on one side along with my website, the other side includes the other information. Please use combination of black, neon green, white, and silver. This needs to catch the eye but yet be clearly visible and legible. Thanks

Industry/Entity Type

Pharmacy

Contact Information for Business Card

It needs to have the following information listed:
Mel's Apothecary Owner/Pharm D.
7134 North Brook Lane
Brookhaven Falls, MN 55390
Phone 605-318-6207
Fax 605-318-6209
email: mel@melsapothecary-example.com
www.melsapothecary-example.com
Store hours Monday-Friday 9 am- 6 pm
Saturday 9 am- 1 pm
Sunday Closed
Please utilize the colors black, white, and neon green, maybe silver.

Requirements
Must have
• It needs to be easily readable!
Nice to have
• It should catch the eye.
Should not have
• Do not use any other colors except listed: black, neon green, white, & silver.

```html
<!DOCTYPE html>
<html lang="en">
<head>
<meta charset="utf-8">
<title>Mel's Apothecary – Business Card</title>
<link href="https://fonts.googleapis.com/css2?family=Open+Sans:wght@400;700&display=swap" rel="stylesheet">
<style>
  :root{
    --bg:#e4e4e4;
    --black:#0b0b0c;
    --white:#ffffff;
    --silver-light:#f7f7f7;
    --silver-mid:#d2d2d2;
    --silver-dark:#a9a9a9;
    --neon:#8ccf2e;
    --ink:#111111;
  }
  *{box-sizing:border-box;margin:0;padding:0}
  html,body{width:1200px;height:1000px;overflow:hidden}
  body{background:var(--bg);font-family:'Open Sans',Arial,sans-serif;position:relative}

  .card{position:absolute;width:560px;height:320px;overflow:hidden;
    box-shadow:0 10px 24px rgba(0,0,0,.18);background:var(--black)}
  .silver{background:linear-gradient(180deg,var(--silver-light) 0%,var(--white) 30%,var(--silver-mid) 70%,var(--silver-dark) 100%)}

  /* Front */
  .card-front{left:560px;top:580px}
  .front-band{position:absolute;left:0;right:0;top:96px;height:128px;display:flex;align-items:center}
  .brand-mark{width:150px;height:100%;display:flex;align-items:center;justify-content:center;border-right:2px solid var(--silver-dark)}
  .brand-dot{width:44px;height:44px;border-radius:50%;background:var(--neon)}
  .brand-text{padding-left:26px}
  .brand-name{font-weight:700;font-size:38px;color:var(--ink);letter-spacing:-.5px;line-height:1.1}
  .brand-url{font-weight:700;font-size:17px;color:var(--ink);margin-top:8px}

  /* Back */
  .card-back{left:80px;top:100px}
  .back-silver{position:absolute;left:0;top:0;bottom:0;width:170px}
  .icon-col{position:absolute;left:128px;top:38px;display:flex;flex-direction:column;gap:17px}
  .icon{width:26px;height:26px;border-radius:50%;background:var(--black);display:flex;align-items:center;justify-content:center}
  .icon svg{width:14px;height:14px;fill:none;stroke:var(--white);stroke-width:1.8}
  .contact{position:absolute;left:196px;top:28px;color:var(--white);font-size:14px;line-height:1.35}
  .contact p{margin-bottom:10px}
</style>
</head>
<body>

<section class="card card-back" aria-label="Business card back">
  <div class="back-silver silver"></div>
  <div class="icon-col">
    <span class="icon"><svg viewBox="0 0 16 16"><circle cx="8" cy="8" r="4"/></svg></span>
    <span class="icon"><svg viewBox="0 0 16 16"><path d="M2 8 L8 2.5 L14 8 M4 7 V14 H12 V7"/></svg></span>
    <span class="icon"><svg viewBox="0 0 16 16"><path d="M4 2 L6.5 2 L7.5 5 L6 6.5 Q7.5 9.5 9.5 10 L11 8.5 L14 9.5 L14 12 Q9 14 5 10 Q2 6 4 2Z"/></svg></span>
    <span class="icon"><svg viewBox="0 0 16 16"><rect x="3" y="6" width="10" height="7"/><path d="M5 6 V2 H11 V6 M5 10 H11"/></svg></span>
    <span class="icon"><svg viewBox="0 0 16 16"><rect x="2" y="4" width="12" height="9"/><path d="M2 4 L8 9 L14 4"/></svg></span>
    <span class="icon"><svg viewBox="0 0 16 16"><circle cx="8" cy="8" r="6"/><path d="M8 4.5 V8 L10.5 9.5"/></svg></span>
  </div>
  <div class="contact">
    <p>Mel's Apothecary Owner/Pharm D.</p>
    <p>7134 North Brook Lane<br>Brookhaven Falls, MN 55390</p>
    <p>Phone 605-318-6207</p>
    <p>Fax 605-318-6209</p>
    <p>email: mel@melsapothecary-example.com</p>
    <p>Store hours<br>Monday-Friday 9 am- 6 pm<br>Saturday 9 am- 1 pm<br>Sunday Closed</p>
  </div>
</section>

<section class="card card-front" aria-label="Business card front">
  <div class="front-band silver">
    <div class="brand-mark"><span class="brand-dot"></span></div>
    <div class="brand-text">
      <div class="brand-name">Mel's Apothecary</div>
      <div class="brand-url">www.melsapothecary-example.com</div>
    </div>
  </div>
</section>

</body>
</html>
```